Breezeway Comfort business cards design

Need a business card design for a Heating and Air Conditioning business. I need these items included.
Business name: Breezeway Comfort
Owner: Marcus Tollefsen
License # 2874590
Phone number # 555-382-4071
Email: breezewaycomfortair@mailvista.example
Sales
Service
Installation
Maintenance

Heating and Air Conditioning

Requirements
Must have
• Company name , license number , phone number , email

```html
<!DOCTYPE html>
<html lang="en">
<head>
<meta charset="utf-8">
<title>Breezeway Comfort – Business Cards</title>
<link rel="stylesheet" href="https://fonts.googleapis.com/css2?family=Poppins:wght@400;600;700;800&display=swap">
<style>
  :root {
    --canvas: #e6e7ea;
    --brand-blue: #1c44a6;
    --white: #ffffff;
    --accent-orange: #f37a2a;
    --accent-red: #e8393f;
    --gold: #f5a623;
    --shadow: 0 14px 30px rgba(20, 30, 60, 0.22);
  }
  * { box-sizing: border-box; margin: 0; padding: 0; }
  html, body {
    width: 1200px; height: 780px; overflow: hidden;
    background: var(--canvas);
    font-family: "Poppins", sans-serif;
  }
  .sheet {
    position: relative; width: 1200px; height: 780px;
    display: flex; align-items: center; justify-content: center; gap: 40px;
  }
  .card {
    position: relative; width: 530px; height: 303px;
    border-radius: 22px; overflow: hidden; box-shadow: var(--shadow);
  }

  /* Front card */
  .card--front { background: var(--brand-blue); }
  .card--front .brand-lockup {
    position: absolute; left: 0; right: 0; top: 96px;
    display: flex; align-items: center; justify-content: center; gap: 12px;
  }
  .brand-dot {
    width: 30px; height: 30px; border-radius: 50%; background: var(--accent-orange); flex: none;
  }
  .card--front .brand-name {
    font-weight: 800; font-size: 32px; color: var(--white);
    letter-spacing: 0.5px; text-transform: uppercase;
  }
  .service-list {
    position: absolute; left: 0; right: 0; bottom: 46px;
    display: flex; justify-content: center; gap: 22px; list-style: none;
  }
  .service-list li {
    display: flex; align-items: center; gap: 7px;
    font-weight: 700; font-size: 14px; color: var(--gold); text-transform: uppercase;
  }
  .service-list li::before {
    content: ""; width: 8px; height: 8px; border-radius: 50%; background: var(--white);
  }

  /* Back card */
  .card--back { background: var(--white); }
  .card--back .wave { position: absolute; inset: 0; }
  .card--back .heading {
    position: absolute; right: 26px; top: 20px;
    font-weight: 800; font-size: 19px; color: var(--accent-red); text-transform: uppercase;
  }
  .card--back .brand-lockup {
    position: absolute; left: 32px; top: 112px;
    display: flex; align-items: center; gap: 8px;
  }
  .card--back .brand-dot { width: 22px; height: 22px; }
  .card--back .brand-name {
    font-weight: 800; font-size: 19px; color: var(--brand-blue); text-transform: uppercase;
    line-height: 1.05; width: 130px;
  }
  .license {
    position: absolute; left: 30px; bottom: 24px; color: var(--white);
  }
  .license-label { font-weight: 600; font-size: 13px; }
  .license-number { font-weight: 800; font-size: 24px; color: var(--gold); letter-spacing: 1.5px; line-height: 1.1; }
  .contact-block {
    position: absolute; left: 262px; top: 132px; color: var(--white);
  }
  .person-name { font-weight: 700; font-size: 23px; line-height: 1.1; }
  .person-role { font-weight: 700; font-size: 14px; color: var(--accent-orange); letter-spacing: 2px; margin-top: 2px; }
  .contact-list { list-style: none; margin-top: 14px; }
  .contact-list li {
    display: flex; align-items: center; gap: 7px;
    font-size: 11px; font-weight: 400; margin-bottom: 6px; white-space: nowrap;
  }
  .contact-list svg { width: 13px; height: 13px; flex: none; }
</style>
</head>
<body>
<main class="sheet">

  <section class="card card--front" aria-label="Card front">
    <div class="brand-lockup">
      <span class="brand-dot"></span>
      <span class="brand-name">Breezeway Comfort</span>
    </div>
    <ul class="service-list">
      <li>Sales</li>
      <li>Service</li>
      <li>Installation</li>
      <li>Maintenance</li>
    </ul>
  </section>

  <section class="card card--back" aria-label="Card back">
    <svg class="wave" viewBox="0 0 530 303" preserveAspectRatio="none" aria-hidden="true">
      <defs>
        <linearGradient id="swoosh" x1="0" y1="1" x2="1" y2="0">
          <stop offset="0" stop-color="#e8393f"/>
          <stop offset="1" stop-color="#f37a2a"/>
        </linearGradient>
      </defs>
      <path d="M0,218 C140,212 195,175 240,128 S390,72 530,68 L530,303 L0,303 Z" fill="#1c44a6"/>
      <path d="M0,211 C140,205 195,168 240,121 S390,65 530,61" fill="none" stroke="url(#swoosh)" stroke-width="4"/>
    </svg>

    <div class="heading">Breezeway Comfort</div>

    <div class="brand-lockup">
      <span class="brand-dot"></span>
      <span class="brand-name">Breezeway Comfort</span>
    </div>

    <div class="license">
      <div class="license-label">LICENSE</div>
      <div class="license-number">2874590</div>
    </div>

    <div class="contact-block">
      <div class="person-name">Marcus Tollefsen</div>
      <div class="person-role">OWNER</div>
      <ul class="contact-list">
        <li>
          <svg viewBox="0 0 24 24" aria-hidden="true"><path fill="#f37a2a" d="M6.6 10.8a15.1 15.1 0 0 0 6.6 6.6l2.2-2.2a1 1 0 0 1 1-.25 11.4 11.4 0 0 0 3.6.57 1 1 0 0 1 1 1V20a1 1 0 0 1-1 1A17 17 0 0 1 3 4a1 1 0 0 1 1-1h3.5a1 1 0 0 1 1 1c0 1.25.2 2.45.57 3.57a1 1 0 0 1-.25 1z"/></svg>
          555-382-4071
        </li>
        <li>
          <svg viewBox="0 0 24 24" aria-hidden="true"><rect x="3" y="5" width="18" height="14" rx="1.5" fill="none" stroke="#f37a2a" stroke-width="2"/><path d="M3.5 6l8.5 7 8.5-7" fill="none" stroke="#f37a2a" stroke-width="2"/></svg>
          breezewaycomfortair@mailvista.example
        </li>
      </ul>
    </div>
  </section>

</main>
</body>
</html>
```